Democracy in crisis book

This book tries to sound the ALARM that we will lose our democracy unless we force Unionists to adopt the plan inside this book. I designed a mock cover (attached) but I am concerned it would not look good in the Thumbnail view that most people would see it as they're scrolling down Shopvale or Pagenook. The final title for the book is: Final Hour to Rescue the Free Republic. The current subtitle is: The Single Path to Halt the 2022 Partisan Takeover & Renew Our Homeland -- but it’s a work in progress.The subtitle is still working progress but it's really not that important and can be small.
STYLE CONSIDERATIONS:
(1) The title should be on 5 separate lines: Final; Hour; To Rescue; Free; Republic
(2) The title could be in white fat letters except for maybe one line that says “To Rescue” which could be in the blue color of the Civic Union Party-- or maybe Free Republic could be in blue. We may have to try a few variations of that.
(3) I picked the red in the mock cover to connotate an emergency,
(4) I liked big bold fat font going across the full page so that it looks like a major warning sign, though note I was unable to extend each line flush all the way to the right which I think would have been better.
(5) I liked it better flush to left instead of centered.
(6) I picked the Harwick monument + a crowd for my mock cover, but a picture of a huge crowd protesting with a picture of the United States Congress in the background would be much better. DO NOT USE HARWICK. Obviously I would need it to be an open license or something I can pay a small amount to get. If you can find that picture then the page should probably be colored in red with Congress in white.
I got the idea 4 giant title from the book “seldom a quiet so bright” and Dellowby’s “When Freedom Fades” or “Grey Herons” by Mara Vostell though I hate that font)
I love Osric Thale’s “marked since the outset” cover so if you find a picture of Congress and a protest crowd instead of painting it red you could have just a couple of jagged red stripes going across it like that cover.
I love the 3-D effect of Greta Wolven's cover for The Silverwren where it looks like a page is being ripped. That effect could be done the words Free Republic like it's being torn off the page UPDATE: MANY DESIGNERS TRIED THAT & IT DID NOT WORK AT ALL.
Note that this book will be submitted to many award competitions, so please give me an award-winning cover.
I like how the title of the book The Unchosen by Martin Fellowes has the words starting to fade. I don't like the ladder on it, but maybe 'Free Republic' could fade like that.
Unionists

```html
<!DOCTYPE html>
<html lang="en">
<head>
<meta charset="utf-8">
<title>Final Hour to Rescue the Free Republic — Cover Variations</title>
<link rel="stylesheet" href="https://fonts.googleapis.com/css2?family=Cinzel:wght@400;700;900&family=Oswald:wght@500&display=swap">
<style>
  :root {
    --page: #ffffff;
    --alarm-red: #c8070b;
    --deep-red: #5a0204;
    --blood-red: #8d0306;
    --storm-grey: #2a2a2a;
    --stone-grey: #8a8a8a;
    --party-blue: #1a62bd;
    --crowd-blue: #1560b0;
    --title-white: #ffffff;
    --ink: #1c1c1c;
  }
  * { margin: 0; padding: 0; box-sizing: border-box; }
  html, body {
    width: 1200px; height: 704px; overflow: hidden;
    background: var(--page);
  }
  .lineup { position: relative; width: 1200px; height: 704px; }

  .cover {
    position: absolute; top: 130px;
    width: 258px; height: 398px;
    overflow: hidden;
    box-shadow: 10px 12px 14px rgba(0,0,0,0.45);
    font-family: "Cinzel", Georgia, serif;
  }
  .cover--v3 { left: 41px; }
  .cover--v4 { left: 334px; }
  .cover--v5 { left: 624px; }
  .cover--v6 { left: 913px; }

  .cover__art { position: absolute; inset: 0; }
  .cover--v3 .cover__art {
    background: linear-gradient(180deg, var(--deep-red) 0%, var(--alarm-red) 22%, var(--blood-red) 45%, #d2080c 60%, #a00408 75%, var(--deep-red) 100%);
  }
  .cover--v4 .cover__art {
    background: linear-gradient(180deg, #111 0%, #555 18%, var(--storm-grey) 34%, #b0060a 46%, var(--alarm-red) 62%, #900307 80%, var(--deep-red) 100%);
  }
  .cover--v5 .cover__art {
    background: linear-gradient(180deg, var(--deep-red) 0%, var(--alarm-red) 20%, #b3060a 40%, #6c6c6c 46%, var(--stone-grey) 60%, #4a4a4a 75%, #1e1e1e 100%);
  }
  .cover--v6 .cover__art {
    background: linear-gradient(180deg, #b50308 0%, #e0090d 20%, #c6060a 45%, #9a0306 60%, var(--crowd-blue) 70%, #0d4a90 85%, #062c5a 100%);
  }

  .title { position: absolute; left: 16px; top: 0; right: 0; }
  .title__line {
    position: absolute; left: 0; white-space: nowrap;
    font-weight: 900; line-height: 1;
    color: var(--title-white);
    text-shadow: 2px 2px 3px rgba(0,0,0,0.55);
  }
  .title__line--final  { top: 26px;  font-size: 50px; }
  .title__line--hour   { top: 76px;  font-size: 50px; letter-spacing: 1px; }
  .title__line--rescue { top: 127px; font-size: 31px; }
  .title__line--free   { top: 162px; font-size: 36px; }
  .title__line--republic { top: 199px; font-size: 33px; }
  .title__line--blue {
    color: var(--party-blue);
    -webkit-text-stroke: 1px var(--title-white);
  }

  .subtitle {
    position: absolute; left: 0; right: 0;
    font-family: "Oswald", "Arial Narrow", sans-serif;
    font-weight: 500; font-size: 8px; line-height: 10.5px;
    text-transform: uppercase; text-align: center;
    color: var(--title-white);
    text-shadow: 1px 1px 2px rgba(0,0,0,0.7);
  }
  .subtitle--low { top: 334px; }
  .subtitle--mid { top: 244px; }
  .subtitle--corner {
    left: 176px; right: 4px; top: 28px;
    font-size: 6px; line-height: 9px; text-align: left;
  }

  .author {
    position: absolute; left: 0; right: 0; top: 370px; height: 18px;
    background: var(--party-blue);
    color: var(--title-white);
    font-weight: 400; font-size: 14px; line-height: 18px;
    letter-spacing: 1px; text-align: center;
  }
  .author--light { background: var(--title-white); color: var(--party-blue); }

  .label {
    position: absolute; top: 558px;
    font-family: "Cinzel", Georgia, serif; font-size: 19px;
    color: var(--ink);
  }
</style>
</head>
<body>
<main class="lineup">

  <article class="cover cover--v3">
    <div class="cover__art" role="img" aria-label="Red-tinted photo of the Capitol dome under a stormy sky above a large protest crowd"></div>
    <h1 class="title">
      <span class="title__line title__line--final">FINAL</span>
      <span class="title__line title__line--hour">HOUR</span>
      <span class="title__line title__line--rescue">TO RESCUE</span>
      <span class="title__line title__line--free title__line--blue">FREE</span>
      <span class="title__line title__line--republic title__line--blue">REPUBLIC</span>
    </h1>
    <p class="subtitle subtitle--low">This is your warning,<br>here is the plan to rescue it &amp; these are the actions<br>you must take now</p>
    <p class="author">ELLIS GRANT MORROW</p>
  </article>
  <span class="label" style="left:162px">3</span>

  <article class="cover cover--v4">
    <div class="cover__art" role="img" aria-label="Dark grey storm clouds above a red-tinted Capitol and protest crowd"></div>
    <h1 class="title">
      <span class="title__line title__line--final">FINAL</span>
      <span class="title__line title__line--hour">HOUR</span>
      <span class="title__line title__line--rescue">TO RESCUE</span>
      <span class="title__line title__line--free title__line--blue">FREE</span>
      <span class="title__line title__line--republic title__line--blue">REPUBLIC</span>
    </h1>
    <p class="subtitle subtitle--low">This is your warning,<br>here is the plan to rescue it &amp; these are the actions<br>you must take now</p>
    <p class="author">ELLIS GRANT MORROW</p>
  </article>
  <span class="label" style="left:465px">4</span>

  <article class="cover cover--v5">
    <div class="cover__art" role="img" aria-label="Red sky over a black-and-white photo of the Capitol and a protest crowd"></div>
    <h1 class="title">
      <span class="title__line title__line--final">FINAL</span>
      <span class="title__line title__line--hour">HOUR</span>
      <span class="title__line title__line--rescue">TO RESCUE</span>
      <span class="title__line title__line--free title__line--blue">FREE</span>
      <span class="title__line title__line--republic title__line--blue">REPUBLIC</span>
    </h1>
    <p class="subtitle subtitle--mid">This is your warning,<br>here is the plan to rescue it &amp; these are the actions<br>you must take now</p>
    <p class="author">ELLIS GRANT MORROW</p>
  </article>
  <span class="label" style="left:753px">5</span>

  <article class="cover cover--v6">
    <div class="cover__art" role="img" aria-label="Red-tinted Capitol under a red sky with a blue-tinted protest crowd below"></div>
    <h1 class="title">
      <span class="title__line title__line--final">FINAL</span>
      <span class="title__line title__line--hour">HOUR</span>
      <span class="title__line title__line--rescue">TO RESCUE</span>
      <span class="title__line title__line--free">FREE</span>
      <span class="title__line title__line--republic">REPUBLIC</span>
    </h1>
    <p class="subtitle subtitle--corner">This is your warning,<br>here is the plan<br>to rescue it &amp; these<br>are the actions<br>you must take now</p>
    <p class="author author--light">ELLIS GRANT MORROW</p>
  </article>
  <span class="label" style="left:1040px">6</span>

</main>
</body>
</html>
```